indépendant en tant que Massothérapeute et Préparateur Mental, j'ai besoin de ...

Massothérapeute et préparateur mental indépendant, je recherche une carte de visite sobre et dynamique, sans images liées au massage ou à la préparation mentale mais intégrant mon logo. Les couleurs que j'aime bien sont : Blanc, gris, anthracite, noir et jaune

carte de préférence Horizontale
neutre qui puisse toucher le deux domaines Massothérapie et préparation mentale

Requirements
Must have
• mon projet doit intégrer au recto:
LOGO
Loïc Bardemaz
078 315 26 48
info@loicbardemaz-exemple.ch
et éventuellement www.loicbardemaz-exemple.ch

et au verso les deux adresses:

Chemin des Grèvelins 7B
1400 Yverdon-les-Bains

Avenue des Mélèzes 9
1700 Fribourg

Should not have
• mon projet ne doit pas contenir d'image en liens avec le massage ni la préparation mentale.

```html
<!DOCTYPE html>
<html lang="fr">
<head>
<meta charset="utf-8">
<title>Loïc Bardemaz – Carte de visite</title>
<link rel="stylesheet" href="https://fonts.googleapis.com/css2?family=Montserrat:wght@400;500;600;700&display=swap">
<style>
  :root {
    --bg: #3a3a3c;
    --anthracite: #221f24;
    --paper: #ffffff;
    --ink: #1f1d20;
    --yellow: #f4c400;
    --light-text: #e9e7ea;
  }
  * { box-sizing: border-box; margin: 0; padding: 0; }
  html, body { width: 1200px; height: 900px; overflow: hidden; }
  body {
    background: var(--bg);
    font-family: "Montserrat", Arial, sans-serif;
    position: relative;
  }
  .card {
    position: absolute;
    left: 240px;
    width: 720px;
    height: 411px;
    box-shadow: 0 10px 30px rgba(0,0,0,.45);
  }
  /* Verso */
  .card--back { top: 30px; background: var(--anthracite); }
  .back-name {
    position: absolute;
    left: 0; right: 0; top: 118px;
    text-align: center;
    color: var(--yellow);
    font-weight: 700;
    font-size: 62px;
    letter-spacing: 1px;
  }
  .addresses {
    position: absolute;
    left: 0; right: 0; bottom: 62px;
    display: flex;
    justify-content: center;
    color: var(--light-text);
    font-size: 14px;
    line-height: 1.35;
    letter-spacing: .3px;
  }
  .address { padding: 0 14px; }
  .address--left { text-align: right; }
  .address-divider { width: 2px; background: var(--yellow); }
  /* Recto */
  .card--front { top: 461px; background: var(--paper); }
  .front-brand { position: absolute; left: 70px; top: 62px; color: var(--ink); }
  .front-brand-name { font-weight: 700; font-size: 34px; letter-spacing: .5px; }
  .front-brand-title {
    margin-top: 4px;
    font-weight: 600;
    font-size: 12px;
    letter-spacing: 1.2px;
    text-transform: uppercase;
  }
  .contact { position: absolute; left: 70px; bottom: 58px; color: var(--ink); }
  .contact-name { font-size: 24px; font-weight: 400; }
  .contact-rule { width: 56px; height: 3px; background: var(--yellow); margin: 8px 0 10px; }
  .contact-line { display: flex; align-items: center; font-size: 17px; line-height: 26px; }
  .contact-line svg { width: 15px; height: 15px; margin-right: 10px; flex: none; }
</style>
</head>
<body>

<section class="card card--back" aria-label="Verso de la carte">
  <div class="back-name">Loïc Bardemaz</div>
  <div class="addresses">
    <p class="address address--left">Chemin des Grèvelins 7B<br>1400 Yverdon-les-Bains</p>
    <span class="address-divider"></span>
    <p class="address">Avenue des Mélèzes 9<br>1700 Fribourg</p>
  </div>
</section>

<section class="card card--front" aria-label="Recto de la carte">
  <div class="front-brand">
    <div class="front-brand-name">Loïc Bardemaz</div>
    <div class="front-brand-title">Massothérapeute / Préparateur Mental</div>
  </div>

  <div class="contact">
    <p class="contact-name">Loïc Bardemaz</p>
    <div class="contact-rule"></div>
    <p class="contact-line">
      <svg viewBox="0 0 16 16" aria-hidden="true"><circle cx="8" cy="8" r="8" fill="#f4c400"/><path d="M5 4.5h1.6l.8 2-1 .7a5 5 0 0 0 2.4 2.4l.7-1 2 .8V11a1 1 0 0 1-1 1A6.5 6.5 0 0 1 4 5.5a1 1 0 0 1 1-1z" fill="#fff"/></svg>
      078 315 26 48
    </p>
    <p class="contact-line">
      <svg viewBox="0 0 16 16" aria-hidden="true"><circle cx="8" cy="8" r="8" fill="#f4c400"/><rect x="4" y="5.2" width="8" height="5.6" rx=".6" fill="#fff"/><path d="M4.3 5.6 8 8.4l3.7-2.8" fill="none" stroke="#f4c400" stroke-width=".9"/></svg>
      info@loicbardemaz-exemple.ch
    </p>
    <p class="contact-line">
      <svg viewBox="0 0 16 16" aria-hidden="true"><circle cx="8" cy="8" r="8" fill="#f4c400"/><g fill="none" stroke="#fff" stroke-width="1"><circle cx="8" cy="8" r="4"/><ellipse cx="8" cy="8" rx="1.8" ry="4"/><path d="M4 8h8"/></g></svg>
      www.loicbardemaz-exemple.ch
    </p>
  </div>
</section>

</body>
</html>
```